Cushion and pillow filling machines

Vellano Macchine it's producer of machines for upholstery and mattress industry, always by innovative projects and pays attention on the productivity and wellness of the operators.We need an idea for introduce our machines for filling pillows or cushion quickly and automatically : " THE SMART WAY to fill your DREAMS!
Cushions and pillow filling, fibre processing, fibre balls forming, blending and much more"

Target Market(s)

PRODUCERS of upholstery and mattresses

Industry/Entity Type

Manufacturer

Font styles to use
Other font styles liked:
• futura bold

Requirements
Must have
• Our company name by true type "futurabold" bordeaux color
• "THE SMART WAY to fill your DREAMS!
• Cushions and pillow filling, fibre processing, fibre balls forming, blending and much more"
• website.: www.vellanomacchine.it
Nice to have
• You can modify the colors of the images, the leaflet design should put the attention to our machines . you can use one or part of the example of layout sent. Please note this graphic will be used in horizontal format.

```html
<!DOCTYPE html>
<html lang="en">
<head>
<meta charset="utf-8">
<title>Vellano Macchine – The Smart Way to Fill Your Dreams</title>
<link href="https://fonts.googleapis.com/css2?family=Jost:wght@300;400;500;700&display=swap" rel="stylesheet">
<style>
  :root {
    --paper: #ffffff;
    --green: #2ea83a;
    --green-dark: #23892d;
    --red: #e0232b;
    --bordeaux: #7d1428;
    --ink: #4a4a4a;
    --grey-soft: #d9dde0;
    --photo-warm: #e9d7c8;
    --photo-cool: #dfe4e8;
    --pillow: #a9adb1;
    --machine: #3b58b0;
  }
  * { margin: 0; padding: 0; box-sizing: border-box; }
  html, body { width: 1200px; height: 798px; overflow: hidden; background: var(--paper); }
  body { font-family: "Jost", "Futura", sans-serif; color: var(--ink); }

  .ad { position: relative; width: 1200px; height: 798px; background: var(--paper); overflow: hidden; }

  .ad__shapes { position: absolute; inset: 0; }

  .photo { position: absolute; }
  .photo--baby {
    left: 40px; top: 150px; width: 470px; height: 420px;
    border-radius: 50% 46% 44% 50%;
    background: radial-gradient(ellipse at 45% 55%, var(--photo-warm) 0%, #f3ece6 55%, var(--photo-cool) 100%);
  }
  .photo--pillows {
    left: 70px; top: 540px; width: 430px; height: 190px;
    border-radius: 40px;
    background: linear-gradient(160deg, #e4e6e8 0%, var(--pillow) 60%, #8e9397 100%);
  }
  .photo--machines {
    left: 610px; top: 560px; width: 540px; height: 150px;
    border-radius: 18px;
    background: linear-gradient(120deg, #eef1f7 0%, #b9c5e6 45%, var(--machine) 100%);
  }

  .brand {
    position: absolute; left: 690px; top: 56px;
    display: flex; align-items: center; gap: 16px;
  }
  .brand__dot { width: 34px; height: 34px; border-radius: 50%; background: var(--red); }
  .brand__name {
    font-weight: 700; font-size: 40px; letter-spacing: 0.5px;
    color: var(--bordeaux); text-transform: uppercase;
  }
  .brand__kicker {
    position: absolute; left: 740px; top: 36px;
    font-size: 16px; letter-spacing: 3px; text-transform: uppercase; color: var(--ink);
  }

  .headline { position: absolute; left: 560px; top: 200px; }
  .headline__lead {
    font-weight: 700; font-size: 74px; line-height: 1; color: var(--red);
    text-transform: uppercase; letter-spacing: -0.5px;
  }
  .headline__row { display: flex; align-items: center; gap: 16px; margin-top: 14px; }
  .headline__sub {
    font-weight: 300; font-size: 40px; color: var(--ink); text-transform: uppercase;
  }
  .headline__dreams {
    background: var(--green); color: var(--paper);
    font-weight: 700; font-size: 48px; line-height: 1;
    padding: 8px 22px 10px; text-transform: uppercase; letter-spacing: 1px;
  }

  .services {
    position: absolute; left: 580px; top: 410px;
    display: grid; grid-template-columns: 250px 260px; column-gap: 40px;
    list-style: none;
  }
  .services__item {
    position: relative; padding-left: 26px;
    font-size: 24px; font-weight: 400; line-height: 1.75; color: var(--ink);
  }
  .services__item::before {
    content: ""; position: absolute; left: 2px; top: 16px;
    width: 10px; height: 10px; border-radius: 50%;
    border: 2px solid var(--green);
  }

  .website {
    position: absolute; right: 60px; bottom: 22px;
    display: flex; align-items: center; gap: 12px;
    color: var(--paper); font-size: 24px; font-weight: 500; letter-spacing: 0.5px;
  }
  .website__icon { width: 24px; height: 24px; }
</style>
</head>
<body>
  <main class="ad">
    <svg class="ad__shapes" width="1200" height="798" viewBox="0 0 1200 798" aria-hidden="true">
      <path class="arc-frame" d="M 560 110 C 330 70, 20 170, 30 420 C 38 560, 110 640, 200 690"
            fill="none" stroke="var(--green)" stroke-width="34" stroke-linecap="round"/>
      <path class="band-bottom" d="M 0 705 C 300 690, 700 700, 1200 660 L 1200 798 L 0 798 Z"
            fill="var(--green)"/>
      <path class="band-bottom-shade" d="M 0 735 C 400 720, 800 725, 1200 700 L 1200 712 C 800 738, 400 734, 0 748 Z"
            fill="var(--green-dark)" opacity="0.5"/>
    </svg>

    <div class="photo photo--baby" role="img" aria-label="Photo of a sleeping baby in a striped knitted hat"></div>
    <div class="photo photo--pillows" role="img" aria-label="Photo of a stack of soft grey pillows"></div>
    <div class="photo photo--machines" role="img" aria-label="Photos of blue and white pillow filling and fibre processing machines"></div>

    <p class="brand__kicker">Italian Technology</p>
    <div class="brand">
      <span class="brand__dot"></span>
      <span class="brand__name">Vellano Macchine</span>
    </div>

    <h1 class="headline">
      <span class="headline__lead">The Smart Way</span>
      <span class="headline__row">
        <span class="headline__sub">to fill your</span>
        <span class="headline__dreams">Dreams</span>
      </span>
    </h1>

    <ul class="services">
      <li class="services__item">Cushions</li>
      <li class="services__item">Fibre Balls Forming</li>
      <li class="services__item">Pillow Filling</li>
      <li class="services__item">Blending</li>
      <li class="services__item">Fibre Processing</li>
      <li class="services__item">Much More</li>
    </ul>

    <p class="website">
      <svg class="website__icon" viewBox="0 0 24 24" aria-hidden="true">
        <circle cx="12" cy="12" r="10" fill="none" stroke="#fff" stroke-width="2"/>
        <circle cx="12" cy="12" r="4" fill="#fff"/>
      </svg>
      www.vellanomacchine.it
    </p>
  </main>
</body>
</html>
```